Layout & infographics for 36p Business Plan

Hello, we're looking for a designer who has knowledge in layouting and simple illustration for our 36 pages Business Plan in the catering supply sector. The work includes the basic layout (photographs, fonts and colours are given and set by us), 5-6 excel diagrams, 4-5 icon or pictureloft illustrations and some this & that.

WE WILL PAY UP TO 280 EUR IF THE AMOUNT AND QUALITY OF WORK NEEDS IT!

We need no frills, but a classic and "nice" design. Examples and our logo are shown in the attachments... people with some knowledge of German language have a clear advantage, but we appreciate all kinds of proposals, as long as the portfolio can convince us. Thanks and good luck, Henrik Tellhaus (Managing Partner)

Target Market(s)

The readers of the business plan come from the catering, trading and venture capital sector, so we want some nice & catchy, but still "traditional" design.

Industry/Entity Type

Catering

Font styles to use
Serif

Colors
33a6d7
0255a3
ffffff
ebf6fa

```html
<!DOCTYPE html>
<html lang="de">
<head>
<meta charset="utf-8">
<title>Business Plan – Layout</title>
<link href="https://fonts.googleapis.com/css2?family=Lato:wght@400;700;900&family=Arimo:wght@400;700&family=Tinos&family=Archivo+Black&display=swap" rel="stylesheet">
<style>
  :root {
    --brand-blue: #33a6d7;
    --band-blue: #1ea7e0;
    --deep-blue: #0255a3;
    --pale-blue: #ebf6fa;
    --white: #ffffff;
    --ink: #1a1a1a;
    --sun: #fff200;
    --caption-blue: #2aa8e0;
  }
  * { box-sizing: border-box; margin: 0; padding: 0; }
  html, body { width: 982px; height: 1200px; overflow: hidden; background: var(--white); }
  .sheet { position: relative; width: 982px; height: 1200px; overflow: hidden; background: var(--white); color: var(--ink); }

  /* Cover */
  .cover-spine { position: absolute; left: 0; top: 0; width: 88px; height: 600px; background: var(--brand-blue); }
  .cover-brand { position: absolute; left: 110px; top: 40px; font-family: "Lato", sans-serif; font-weight: 400; font-size: 36px; letter-spacing: -1px; color: var(--deep-blue); display: flex; align-items: center; gap: 10px; }
  .cover-brand .dot { width: 12px; height: 12px; border-radius: 50%; background: var(--brand-blue); }
  .cover-rule { position: absolute; left: 90px; top: 113px; width: 373px; height: 3px; background: var(--brand-blue); }
  .cover-kicker { position: absolute; left: 294px; top: 121px; font-family: "Lato", sans-serif; font-weight: 700; font-size: 16px; color: var(--ink); }
  .cover-emblem { position: absolute; left: 210px; top: 318px; }
  .cover-title { position: absolute; left: 148px; top: 208px; font-family: "Lato", sans-serif; font-weight: 700; color: var(--ink); line-height: 1; }
  .cover-title .lead { display: block; font-size: 22px; margin-bottom: 4px; }
  .cover-title .main { display: block; font-size: 45px; line-height: 45px; letter-spacing: -0.5px; }
  .cover-date { position: absolute; left: 0; width: 546px; top: 480px; text-align: center; font-family: "Lato", sans-serif; font-weight: 700; font-size: 18px; }
  .cover-authors { position: absolute; left: 0; width: 550px; top: 534px; text-align: center; font-family: "Lato", sans-serif; font-weight: 700; font-size: 13.5px; line-height: 17px; }

  /* Inside front */
  .inside-front { position: absolute; left: 532px; top: 0; width: 431px; height: 600px; background: var(--brand-blue); }
  .inside-front-label { position: absolute; left: 0; width: 100%; text-align: center; font-family: "Archivo Black", sans-serif; font-size: 52px; letter-spacing: 4px; color: #050505; }
  .inside-front-label.top { top: 92px; }
  .inside-front-label.bottom { top: 256px; }

  /* Inner pages */
  .page { position: absolute; font-family: "Arimo", sans-serif; }
  .page-left { left: 88px; top: 640px; width: 350px; height: 560px; overflow: hidden; }
  .page-right { left: 520px; top: 615px; width: 440px; height: 585px; overflow: hidden; }
  .chapter { font-weight: 700; font-size: 10.5px; margin-left: 16px; line-height: 14px; }
  .chapter + .chapter { margin-top: 0; }
  .section-band { background: var(--band-blue); color: var(--ink); font-weight: 700; font-size: 14px; height: 21px; line-height: 21px; padding-left: 16px; margin: 6px 0 9px; }
  .copy { font-size: 9.6px; line-height: 12.2px; padding: 0 16px; color: #111; }
  .copy.serif { font-family: "Tinos", serif; font-size: 9.9px; }
  .copy + .chapter { margin-top: 9px; }

  .chart { margin-left: 150px; display: block; }
  .chart-caption { margin-left: 150px; font-family: "Lato", sans-serif; font-size: 9.5px; line-height: 12px; color: var(--caption-blue); margin-top: 4px; }
  .chart-caption .source { font-family: "Tinos", serif; }
  .page-right .copy { padding: 0 12px 0 132px; margin-top: 20px; }
  .page-right .section-band { margin-top: 9px; padding-left: 132px; }
  .page-right .copy.after-band { margin-top: 0; }
</style>
</head>
<body>
<div class="sheet">

  <!-- Cover -->
  <div class="cover-spine"></div>
  <div class="cover-brand"><span>kuechenwerk.de</span><span class="dot"></span></div>
  <div class="cover-rule"></div>
  <div class="cover-kicker">BUSINESS PLAN</div>
  <svg class="cover-emblem" width="130" height="130" viewBox="0 0 130 130" aria-hidden="true">
    <circle cx="65" cy="65" r="57" fill="var(--sun)" stroke="var(--band-blue)" stroke-width="11"/>
  </svg>
  <h1 class="cover-title">
    <span class="lead">The</span>
    <span class="main">Catering</span>
    <span class="main">Marketing</span>
    <span class="main">Focus</span>
    <span class="main">Plan</span>
  </h1>
  <div class="cover-date">September 12, 2014</div>
  <div class="cover-authors">Lorenz Albrecht<br>Ina Feldmann</div>

  <!-- Inside front -->
  <div class="inside-front">
    <div class="inside-front-label top">INSIDE</div>
    <div class="inside-front-label bottom">FRONT</div>
  </div>

  <!-- Page: market situation -->
  <section class="page page-left">
    <p class="chapter">2. Marktsituation</p>
    <p class="chapter">2.1. Generelle Faktoren</p>
    <h2 class="section-band">Wirtschaftslage und Konsumnachfrage</h2>
    <p class="copy">Der deutschen Wirtschaft geht es gut. Nach der Finanzkrise 2009 scheint das Tal von Unsicherheit und Stagnierung innerhalb der deutschen Volkswirtschaft 2013 erstmals wirklich überwunden worden zu sein. Vor allem die Verbraucher blicken nach vorn – so ist der KVM-Konsumklimaindex innerhalb des ersten Quartals 2014 gegenüber dem Vorjahr um 25% gestiegen, mit weiterem Raum nach oben. Auch die Bruttoinvestitionen der Gewerbe nehmen nach einigen vorsichtigen Jahren wieder zu. 78% des Handels und der Industrie wollen ihr bisheriges Investitionsniveau halten oder erhöhen, so eine Umfrage des WFI-Institutes Bonn vom Frühjahr 2014. Eine Frage dieses bekundeten Zuwachses dürfte jedoch sein, inwieweit sich die Mehrausgaben auch bei der Bruttoinlandsnachfrage des privaten Konsums bemerkbar machen werden. Der Großteil der hiesigen Marktforschungsinstitute prognostizieren hier nach verhaltenen Wachstumsraten von 0,5-1,2% nun erstmals wieder optimistischere Zahlen um die 2% für 2014 – gemessen am Bruttoinlandsprodukt entspricht dies einem wertmäßigem Zuwachs von ca. 55 Mrd. EUR. Diese günstigere Ausgangslage macht sich auch in der gesunkenen Zahl der gewerblichen Insolvenzen sichtbar, die im Dezember 2013 auf dem niedrigsten Stand seit 6 Jahren war. Gemeinsam sprechen diese Daten für eine deutliche Erholung der Gesamtwirtschaft und einer Steigerung der Ausgabenneigung der Verbraucher – ein günstiges Klima für Unternehmen und Firmengründungen im Jahr 2014, die sich auf den deutschen (Online-)Handel fokussieren.</p>
    <p class="chapter">2.2. Die Entwicklung der Gastronomiebranche</p>
    <h2 class="section-band">Marktsituation und Hintergründe</h2>
    <p class="copy">Von der allgemeinen Erholung der deutschen Volkswirtschaft und der privaten Konsumneigung profitierte 2013 nicht zuletzt auch der Gastronomiesektor – hier sind die Umsätze im gegenüber 2012 um 3% gestiegen, in einzelnen Sparten waren sogar an die 6%. Die ca. 180.000 angemeldeten Gastgewerbe (ohne Beherbergung), Imbissbetriebe, Caterer, Franchise-Restaurants, Diskotheken, Bars u.a. erwirtschafteten mit knapp einer Mio. sozialversicherungspflichtig Beschäftigten in 2013 einen Umsatz von gut 38 Mrd. EUR. Nach einem sichtbaren Einbruch durch die Finanzkrise 2009 und der daraus resultierenden Unsicherheit der Konsumenten in Sachen Freizeitausgaben haben sich die Umsätze wieder erholt und sind im letzten Jahr um knapp 3% auf das ungefähre Vorkrisenniveau gewachsen (siehe Grafik).</p>
    <p class="copy serif">Dieser Zuwachs speist sich zum Großteil aus höheren Durchschnittsbons, d.h. aus gestiegenen durchschnittlich Ausgaben der Gäste pro Einzelbesuch, weniger aus höheren Besucherzahlen oder gestiegenen Preisen. Für die Branche, als auch für das Konzept von Kuechenwerk hat dies zwei Auswirkungen: Einerseits kann der durch den Preisanstieg der Beschaffungsware und der Energiepreise</p>
  </section>

  <!-- Page: chart and segment development -->
  <section class="page page-right">
    <svg class="chart" width="205" height="140" viewBox="0 0 205 140" role="img" aria-label="Balkendiagramm: offene Stellen nach Branche, drei Zeiträume">
      <text x="0" y="6" font-family="Arimo, sans-serif" font-size="4.6" fill="#333">Job openings by sector, 2011–2012</text>
      <text x="0" y="11" font-family="Arimo, sans-serif" font-size="3.6" fill="#555">(in thousands)</text>
      <g font-family="Arimo, sans-serif" font-size="3.4" fill="#444">
        <rect x="6" y="15" width="4" height="3" fill="#a9c8ea"/><text x="11" y="17.6">Nov 2011</text>
        <rect x="28" y="15" width="4" height="3" fill="#4a7fc4"/><text x="33" y="17.6">Oct 2012</text>
        <rect x="50" y="15" width="4" height="3" fill="#1d3f7a"/><text x="55" y="17.6">Nov 2012</text>
      </g>
      <g stroke="#ddd" stroke-width="0.4">
        <line x1="14" y1="30" x2="200" y2="30"/><line x1="14" y1="55" x2="200" y2="55"/>
        <line x1="14" y1="80" x2="200" y2="80"/><line x1="14" y1="105" x2="200" y2="105"/>
      </g>
      <line x1="14" y1="130" x2="200" y2="130" stroke="#888" stroke-width="0.5"/>
      <g font-family="Arimo, sans-serif" font-size="3.4" fill="#555" text-anchor="end">
        <text x="11" y="31">800</text><text x="11" y="56">600</text><text x="11" y="81">400</text><text x="11" y="106">200</text><text x="11" y="131">0</text>
      </g>
      <g>
        <rect x="20" y="56" width="5" height="74" fill="#a9c8ea"/><rect x="25" y="49" width="5" height="81" fill="#4a7fc4"/><rect x="30" y="41" width="5" height="89" fill="#1d3f7a"/>
        <rect x="43" y="47" width="5" height="83" fill="#a9c8ea"/><rect x="48" y="44" width="5" height="86" fill="#4a7fc4"/><rect x="53" y="44" width="5" height="86" fill="#1d3f7a"/>
        <rect x="66" y="55" width="5" height="75" fill="#a9c8ea"/><rect x="71" y="47" width="5" height="83" fill="#4a7fc4"/><rect x="76" y="56" width="5" height="74" fill="#1d3f7a"/>
        <rect x="89" y="71" width="5" height="59" fill="#a9c8ea"/><rect x="94" y="70" width="5" height="60" fill="#4a7fc4"/><rect x="99" y="67" width="5" height="63" fill="#1d3f7a"/>
        <rect x="112" y="84" width="5" height="46" fill="#a9c8ea"/><rect x="117" y="85" width="5" height="45" fill="#4a7fc4"/><rect x="122" y="86" width="5" height="44" fill="#1d3f7a"/>
        <rect x="135" y="99" width="5" height="31" fill="#a9c8ea"/><rect x="140" y="95" width="5" height="35" fill="#4a7fc4"/><rect x="145" y="96" width="5" height="34" fill="#1d3f7a"/>
        <rect x="158" y="117" width="5" height="13" fill="#a9c8ea"/><rect x="163" y="115" width="5" height="15" fill="#4a7fc4"/><rect x="168" y="116" width="5" height="14" fill="#1d3f7a"/>
      </g>
      <g font-family="Arimo, sans-serif" font-size="3.4" fill="#444" text-anchor="middle">
        <text x="28" y="135">Retail</text><text x="51" y="135">Health</text><text x="74" y="135">Services</text>
        <text x="97" y="135">Leisure</text><text x="120" y="135">Public</text><text x="143" y="135">Industry</text><text x="166" y="135">Building</text>
      </g>
    </svg>
    <p class="chart-caption">Grafik: Umsatz im Gastgewerbe (ohne Beherbergung) in Mrd. EUR<br><span class="source">Quelle: GVBD, Statistisches Zentralamt</span></p>
    <p class="copy serif" style="margin-top:18px;padding-left:132px;">entstandene Kostendruck nicht wirklich auf die Gäste umgewälzt werden. Gerade im unteren Preissegment spüren viele Gastronomen einen gehörigen Druck auf die Rentabilität. <span style="font-family:Arimo,sans-serif;font-size:9.6px">Auf der anderen Seite bedeutet das, dass die Gäste durchaus höhere Einzelbons in Kauf nehmen, sobald ihnen besondere Leistungen geboten werden. So belegen Ernährungsstudie wie die von Alpenhof aus dem Jahr 2012, dass die Preissensibilität der Gäste just in dem Moment nachlässt, in dem gastronomische Betriebe hinsichtlich Speisen, Service und Ambiente etwas Besonderes bieten, womit man sich – ganz unabhängig vom Preis – auch im Alltag belohnen kann. Die Konsumenten sind also durchaus kostenbewusst – bei wirklichen Zusatzleistungen, die durch die Gastronomie geschaffen werden, werden allerdings auch höhere Ausgaben gerne in Kauf genommen. Diese, unter dem Strich auch positiv zu verstehende Entwicklung macht sich zusammen mit einem allgemeinen Trend zum Außer-Haus Konsum auch im steigenden Anteil der Gastronomieumsätze an den gesamten Konsumausgaben bemerkbar. Nach Werten um die 4,5% im Krisenjahr 2009 geben die Konsumenten in Deutschland mittlerweile knapp 6% ihres gesamten verfügbaren Einkommens für gastronomische Leistungen aus – dies ist ca. ein Drittel ihres gesamten Ernährungsbudgets.</span></p>
    <h2 class="section-band">Spartenentwicklung und Anbieterstruktur</h2>
    <p class="copy after-band">Von diesen gestiegenen Ausgaben profitieren jedoch nicht alle Gastronomiesegmente gleichermaßen. Während einige Segmente wie die getränkegeprägte Gastronomie seit Jahren unter rückgängigen Besuchen</p>
  </section>

</div>
</body>
</html>
```